Electrical company business card design.

Hi, were an electrical company in Auckland New Zealand called Quarneth Ltd. We focus mainly on high end residential and commercial so the card would be targeted towards that.
The card will be for myself, i am the director of the company.
Name: Derek Olstow
Position: Director/electrician
Phone: 021 387 9415
Email: derek@quarneth.co.nz
Location: Auckland
As for colors the the blue color in the logo is preferred, i also don't mind a black background option.
Target Market(s)
High end residential and commercial
Industry/Entity Type
Electrician
Contact Information for Business Card
Name: Derek Olstow Position: Director/Electrician Phone: 021 387 9415, Email: derek@quarneth.co.nz, Location: Auckland

```html
<!DOCTYPE html>
<html lang="en">
<head>
<meta charset="utf-8">
<title>Quarneth Ltd – Business Card</title>
<link rel="stylesheet" href="https://fonts.googleapis.com/css2?family=Exo+2:wght@400;600;700;800&display=swap">
<style>
  :root {
    --page-bg: #f7f9fd;
    --front-navy: #04044a;
    --back-black: #03041a;
    --brand-blue: #1a8fe0;
    --brand-deep: #2a3fa8;
    --text-white: #ffffff;
    --rule: rgba(255, 255, 255, 0.75);
    --card-shadow: 6px 10px 10px rgba(0, 0, 0, 0.35);
  }
  * { margin: 0; padding: 0; box-sizing: border-box; }
  html, body {
    width: 1200px; height: 1000px; overflow: hidden;
    background: var(--page-bg);
    font-family: "Exo 2", sans-serif;
    color: var(--text-white);
  }
  .canvas { position: relative; width: 1200px; height: 1000px; }

  .card {
    position: absolute;
    width: 700px; height: 400px;
    border-radius: 34px;
    box-shadow: var(--card-shadow);
    overflow: hidden;
  }
  .card--front {
    left: 71px; top: 62px;
    background: radial-gradient(circle at 58% 45%, #0c0c5c 0%, var(--front-navy) 55%);
  }
  .card--back {
    left: 427px; top: 541px;
    background: linear-gradient(100deg, #05112a 0%, var(--back-black) 45%, var(--back-black) 100%);
  }

  .brand { position: absolute; inset: 0; }
  .brand__mark {
    position: absolute; border-radius: 50%;
    background: linear-gradient(135deg, var(--brand-blue), var(--brand-deep));
  }
  .brand__name {
    position: absolute; white-space: nowrap;
    font-weight: 600; letter-spacing: 0.02em; line-height: 1;
    color: var(--text-white);
  }
  .brand__tagline {
    position: absolute; white-space: nowrap;
    font-weight: 800; letter-spacing: 0.1em; line-height: 1;
    color: var(--text-white);
  }

  /* front */
  .card--front .brand__mark { left: 110px; top: 151px; width: 100px; height: 100px; }
  .card--front .brand__name { left: 240px; top: 141px; font-size: 68px; }
  .card--front .brand__tagline { left: 241px; top: 234px; font-size: 25px; }

  /* back */
  .card--back .brand__mark { left: 350px; top: 84px; width: 50px; height: 50px; }
  .card--back .brand__name { left: 418px; top: 78px; font-size: 37px; }
  .card--back .brand__tagline { left: 419px; top: 126px; font-size: 13.5px; }

  .divider {
    position: absolute; left: 304px; top: 158px;
    width: 344px; height: 1px; background: var(--rule);
  }
  .person { position: absolute; left: 298px; top: 168px; }
  .person__name {
    font-weight: 700; font-size: 48px; line-height: 1; white-space: nowrap;
  }
  .person__role {
    margin-top: 0; line-height: 1.2;
    font-weight: 400; font-size: 23px; white-space: nowrap;
  }
  .contact { position: absolute; left: 298px; top: 260px; list-style: none; }
  .contact__item {
    display: flex; align-items: center; gap: 8px;
    height: 28px; margin-bottom: 9px;
    font-size: 24px; font-weight: 400; white-space: nowrap;
  }
  .contact__icon { width: 28px; height: 28px; flex: none; }
</style>
</head>
<body>
<main class="canvas">

  <section class="card card--front" aria-label="Business card front">
    <div class="brand">
      <span class="brand__mark" aria-hidden="true"></span>
      <span class="brand__name">QUARNETH</span>
      <span class="brand__tagline">ENERGY WITH EXACTNESS</span>
    </div>
  </section>

  <section class="card card--back" aria-label="Business card back">
    <div class="brand">
      <span class="brand__mark" aria-hidden="true"></span>
      <span class="brand__name">QUARNETH</span>
      <span class="brand__tagline">ENERGY WITH EXACTNESS</span>
    </div>
    <div class="divider"></div>
    <div class="person">
      <h1 class="person__name">DEREK OLSTOW</h1>
      <p class="person__role">Director / Electrician</p>
    </div>
    <ul class="contact">
      <li class="contact__item">
        <svg class="contact__icon" viewBox="0 0 28 28" aria-hidden="true">
          <circle cx="14" cy="14" r="14" fill="#fff"/>
          <path d="M9.5 7.5l2.6 0.2 1.2 3.4-1.7 1.4c0.8 1.8 2.1 3.1 3.9 3.9l1.4-1.7 3.4 1.2 0.2 2.6c-0.6 1.3-1.8 2-3.2 1.8-5.2-0.8-8.6-4.2-9.4-9.4-0.2-1.4 0.5-2.6 1.6-3.4z" fill="var(--back-black)"/>
        </svg>
        <span>021 387 9415</span>
      </li>
      <li class="contact__item">
        <svg class="contact__icon" viewBox="0 0 28 28" aria-hidden="true">
          <circle cx="14" cy="14" r="14" fill="#fff"/>
          <path d="M14 6.5c-3.3 0-5.8 2.5-5.8 5.7 0 4 5.8 9.8 5.8 9.8s5.8-5.8 5.8-9.8c0-3.2-2.5-5.7-5.8-5.7z" fill="var(--back-black)"/>
          <circle cx="14" cy="12.2" r="2.2" fill="#fff"/>
        </svg>
        <span>AUCKLAND</span>
      </li>
    </ul>
  </section>

</main>
</body>
</html>
```